Business Card for Web Design consulting firm

Business card designs for Web Design consulting firm

Target Market(s)

English speaking adults ages 30 - 60. Predominantly professional services eg. Doctor, Dentist

Industry/Entity Type

Consulting

Requirements
Must have
• Double sided card

```html
<!DOCTYPE html>
<html lang="en">
<head>
<meta charset="utf-8">
<title>Veloria Business Card</title>
<link rel="stylesheet" href="https://fonts.googleapis.com/css2?family=Gentium+Book+Plus:wght@400;700&display=swap">
<style>
  :root {
    --page-bg: #ffffff;
    --card-bg: #000000;
    --accent: #f7941d;
    --text-font: "Gentium Book Plus", Georgia, serif;
  }
  * { margin: 0; padding: 0; box-sizing: border-box; }
  html, body {
    width: 1200px;
    height: 881px;
    overflow: hidden;
    background: var(--page-bg);
  }
  .canvas {
    position: relative;
    width: 1200px;
    height: 881px;
  }
  .card {
    position: absolute;
    top: 48px;
    width: 442px;
    height: 736px;
    background: var(--card-bg);
  }
  .card--front { left: 97px; }
  .card--back { left: 589px; }

  .brand-name {
    position: absolute;
    font-family: var(--text-font);
    font-weight: 400;
    color: var(--accent);
    white-space: nowrap;
  }
  .card--front .brand-name {
    left: 0;
    right: 0;
    top: 328px;
    text-align: center;
    font-size: 62px;
    letter-spacing: 10px;
    padding-left: 10px;
  }
  .card--back .brand-name {
    left: 60px;
    top: 76px;
    font-size: 15px;
    letter-spacing: 2px;
  }

  .contact {
    position: absolute;
    right: 72px;
    top: 556px;
    text-align: right;
    font-family: var(--text-font);
    color: var(--accent);
    font-size: 21px;
    line-height: 31px;
    letter-spacing: 2.5px;
    list-style: none;
  }
  .contact__name {
    font-weight: 700;
    letter-spacing: 3px;
    margin-bottom: 2px;
  }
</style>
</head>
<body>
<main class="canvas">
  <section class="card card--front" aria-label="Card front">
    <div class="brand-name">VELORIA</div>
  </section>

  <section class="card card--back" aria-label="Card back">
    <div class="brand-name">VELORIA</div>
    <ul class="contact">
      <li class="contact__name">Your Name</li>
      <li>p (555) 555-5555</li>
      <li>f (555) 555-5555</li>
      <li>yourname@example.com</li>
      <li>www.website.com</li>
    </ul>
  </section>
</main>
</body>
</html>
```